Flyer for Addiction program

Hi There,There are two parts to this project.1. A double-sided flyer for my next 5-day treatment program for addictions and family trauma.2. A one-page cover for the front of the course folders to match the above flyer?I have put together an information folder. Here is the filecrate link;https://www.filecrate.com/sh/jn7lkly6wcqphpt/AACmad0pag08NeuT2pM27USPa?dl=0Included in the information folder is;1. Copy2. Selection of images3. Logos and Brand identity kit4. Examples of past flyers and folder coverPlease don't hesitate to contact me if you have any questions.RegardsRebecca

Colors

Designer to choose colors to be used in the design.

Requirements
Must have
• 2 pages flyer please.
• Contemporary / fresh design

```html
<!DOCTYPE html>
<html lang="en">
<head>
<meta charset="utf-8">
<title>Breaking the Family Trance – 5 day program flyer</title>
<link href="https://fonts.googleapis.com/css2?family=Open+Sans:wght@700;800&family=Source+Sans+3:wght@400;600;700&display=swap" rel="stylesheet">
<style>
  :root{
    --stage:#a9abac;
    --navy:#13203a;
    --navy-soft:#1d2c49;
    --orange:#f08a1c;
    --ink:#2a2f38;
    --muted:#5b616b;
    --paper:#ffffff;
    --paper-fade:#dfe2e7;
    --footer-text:#b9c0cc;
  }
  *{margin:0;padding:0;box-sizing:border-box}
  html,body{width:1200px;height:894px;overflow:hidden}
  body{background:var(--stage);position:relative;font-family:"Source Sans 3",Arial,sans-serif;color:var(--ink)}

  .page{position:absolute;top:97px;width:476px;height:673px;background:var(--navy);overflow:hidden}
  .page--front{left:95px}
  .page--back{left:629px}

  .hero-photo{position:absolute;left:0;top:0;width:476px;height:300px}
  .page--front .hero-photo{background:linear-gradient(180deg,#6b5a48 0%,#8a7662 35%,#4a4340 70%,var(--navy) 100%)}
  .page--back .hero-photo{background:linear-gradient(180deg,#3e4a3c 0%,#56634a 35%,#3a3f3a 65%,var(--navy) 100%)}

  .snapshot{position:absolute;background:#f4f4f2;padding:5px;box-shadow:0 2px 6px rgba(0,0,0,.35)}
  .snapshot span{display:block;width:100%;height:100%}
  .snap-a{left:372px;top:92px;width:104px;height:76px;transform:rotate(14deg)}
  .snap-a span{background:linear-gradient(135deg,#9a9a98,#4e4e4e)}
  .snap-b{left:340px;top:150px;width:106px;height:80px;transform:rotate(6deg)}
  .snap-b span{background:linear-gradient(135deg,#8b8b89,#3f3f3f)}
  .snap-c{left:300px;top:104px;width:124px;height:98px;transform:rotate(4deg)}
  .snap-c span{background:linear-gradient(135deg,#7d8a83,#3b4a52)}
  .snap-d{left:381px;top:168px;width:92px;height:70px;transform:rotate(-5deg)}
  .snap-d span{background:linear-gradient(135deg,#8aa06a,#5b6a48)}

  .title{position:absolute;left:34px;top:20px;color:#fff}
  .title h1{font-family:"Open Sans",Arial,sans-serif;font-weight:800;font-size:29px;line-height:36px;letter-spacing:.2px}
  .title p{font-family:"Open Sans",Arial,sans-serif;font-weight:700;font-size:20px;line-height:26px;margin-top:-2px}

  .panel{position:absolute;left:16px;top:182px;width:446px;height:428px;
    background:linear-gradient(180deg,var(--paper) 0%,var(--paper) 45%,var(--paper-fade) 100%);
    clip-path:polygon(0 0,100% 0,100% 96%,97% 97.5%,94% 95.5%,90% 97%,85% 95%,80% 96.5%,74% 94.5%,69% 97%,64% 95%,58% 96.3%,53% 94.6%,48% 97.2%,42% 95.3%,37% 96.8%,31% 94.8%,26% 96.6%,20% 95%,14% 97.3%,9% 95.4%,4% 96.7%,0 95.2%)}
  .page--front .panel{z-index:1}
  .snapshots{position:absolute;inset:0;z-index:2}
  .clip{position:absolute;left:14px;top:175px;z-index:3}

  .block{position:absolute;z-index:3;font-size:8.6px;line-height:11.2px;color:var(--ink)}
  .quote{left:36px;top:202px;width:270px;font-size:9.4px;line-height:11.6px;color:#111}
  .intro{left:36px;top:240px;width:400px;font-size:9.4px;line-height:11.6px;color:#111}
  .rule{position:absolute;height:0;border-top:1px dotted #b8bcc3}
  .front-rule{left:36px;top:275px;width:404px;z-index:3}
  .lead{left:36px;top:290px;width:408px}
  .heading{font-weight:700;font-size:9.2px;color:var(--orange);text-transform:uppercase;letter-spacing:-.1px}
  .questions{left:36px;top:336px;width:410px}
  .questions .heading{margin-bottom:1px}
  .bullets{list-style:none;margin-top:4px}
  .bullets li{position:relative;padding-left:13px;margin-bottom:1.6px}
  .bullets li::before{content:"";position:absolute;left:0;top:2px;width:6px;height:6px;border:1px solid var(--orange);border-radius:50%}
  .bullets li::after{content:"";position:absolute;left:2px;top:4px;width:2px;height:2px;border-top:1px solid var(--orange);border-right:1px solid var(--orange);transform:rotate(45deg)}
  .undo{left:36px;top:516px;width:410px}
  .undo .heading{text-transform:none;font-size:8.6px}

  .footer{position:absolute;left:34px;top:618px;font-size:7.4px;line-height:11.2px;color:var(--footer-text);letter-spacing:.3px}
  .brand{position:absolute;right:18px;top:630px;display:flex;flex-direction:column;align-items:center;gap:6px}
  .brand i{display:block;width:22px;height:22px;border-radius:50%;background:#8c95a6}
  .brand span{font-size:9px;letter-spacing:2.4px;color:var(--footer-text);text-transform:uppercase}

  .col{position:absolute;z-index:3;font-size:8.6px;line-height:10.8px}
  .benefits{left:31px;top:212px;width:205px}
  .benefits .sub{margin:2px 0 2px}
  .benefits .bullets li{margin-bottom:3px}
  .history{left:31px;top:480px;width:205px}
  .history h3{font-size:10px;font-weight:600;color:var(--navy);margin-bottom:7px}
  .history p{text-align:justify}
  .details{left:250px;top:212px;width:206px}
  .details h4{font-size:8.8px;font-weight:700;color:var(--navy);margin-bottom:3px}
  .details .dates{font-weight:700;color:#111}
  .details p{text-align:justify}
  .details section{margin-bottom:12px}
  .details .rule{position:static;margin:0 0 11px}
  .details .heading{margin-bottom:12px}
</style>
</head>
<body>

<article class="page page--front">
  <div class="hero-photo" role="img" aria-label="Photo of an adult and child walking side by side in boots on a dirt path"></div>
  <header class="title">
    <h1>BREAKING<br>THE FAMILY<br>TRANCE</h1>
    <p>5 day program</p>
  </header>

  <div class="panel"></div>
  <div class="snapshots">
    <div class="snapshot snap-a" role="img" aria-label="Old black and white family photograph"><span></span></div>
    <div class="snapshot snap-b" role="img" aria-label="Old black and white group photograph"><span></span></div>
  </div>
  <svg class="clip" width="16" height="38" viewBox="0 0 16 38" aria-hidden="true">
    <path d="M10 4 L4 30 A4 4 0 0 0 12 32 L16 10 A6 6 0 0 0 4 8 L0 26" fill="none" stroke="var(--orange)" stroke-width="2"/>
  </svg>

  <p class="block quote">”If you cannot get rid of the family skeleton, you may as well make it dance” - Edmund Hartley Crane</p>
  <p class="block intro">“Breaking the Family Trance” and breaking out of your adapted family rolesis one of the most important things you can do to feel happy with yourself and in your relationships.</p>
  <div class="rule front-rule"></div>
  <p class="block lead">Participating in Breaking the Family Trance will help you uncover the unconscious psychological defences, which create destructive habits and behaviour patterns that keep you stuck; recycling the same unfulfilling relationships, circumstances and patterns in your life.</p>

  <div class="block questions">
    <h2 class="heading">How do you know if you need to break free?</h2>
    <p>Consider the following questions:</p>
    <ul class="bullets">
      <li>Do you struggle to meet your own needs and wants, placing friends and family first?</li>
      <li>Do you adapt to fit in, be liked or accepted?</li>
      <li>Are you the one who is overly responsible for others or at work?</li>
      <li>Are you an over achiever only to find you are never satisfied with the end result?</li>
      <li>Do you suffer from repetitive, frustrating situations and unhealthy behaviours in your personal and professional relationships?</li>
      <li>Are you “the one “who listens to others download their problems?</li>
      <li>Do you feel uncomfortable, asking others for help?</li>
      <li>Are you tired of being invisible?</li>
      <li>Do you find yourself feeling compelled to distract others, or use humour to ease emotional tension?</li>
      <li>Are you tired of searching for what you can DO or acquire to feel happy and satisfied?</li>
    </ul>
  </div>

  <div class="block undo">
    <h2 class="heading">Maybe it’s time to think about what you can undo!</h2>
    <p>If you answered yes to any of the above questions, it’s likely that you are carrying a family legacy and a family role from your formative years that does not belong to you. If you seem to be sabotaging your success these roles and unconscious family patterns may very well be getting in the way of your happiness and well being.</p>
  </div>

  <footer class="footer">
    The Tallowood Group Pty Ltd.<br>
    ABN 41 302 118 764 Fernhill Road, Ashby NSW 2799<br>
    Phone: 0491 570 156<br>
    Email: marjorie@thetallowoodgroup.example
  </footer>
  <div class="brand"><i></i><span>Tallowood Group</span></div>
</article>

<article class="page page--back">
  <div class="hero-photo" role="img" aria-label="Photo of a family toasting food over a campfire beside a lake"></div>
  <div class="panel"></div>
  <div class="snapshots">
    <div class="snapshot snap-c" role="img" aria-label="Photo of a young man sitting outdoors"><span></span></div>
    <div class="snapshot snap-d" role="img" aria-label="Photo of a family playing in a grassy field"><span></span></div>
  </div>
  <svg class="clip" width="16" height="38" viewBox="0 0 16 38" aria-hidden="true">
    <path d="M10 4 L4 30 A4 4 0 0 0 12 32 L16 10 A6 6 0 0 0 4 8 L0 26" fill="none" stroke="var(--orange)" stroke-width="2"/>
  </svg>

  <div class="col benefits">
    <h2 class="heading">Program Benefits</h2>
    <p class="sub">During the program you will learn how to:</p>
    <ul class="bullets">
      <li>Recognise the ways you adapt, so you can undo the false you and unleash the true you.</li>
      <li>Identify what you need to do for yourself to stop destructive behaviour patterns.</li>
      <li>Uncover important values that will bring you deep fulfilment.</li>
      <li>Speak up and be heard.</li>
      <li>Be present and be seen.</li>
      <li>Ask for help without feeling too embarrassed or vulnerable.</li>
      <li>Manage your emotions, rather than everyone else’s.</li>
      <li>Share responsibility with others and have more equal relationships.</li>
      <li>Discover what you really need and want, and learn the strategy of creating a vision</li>
      <li>Discover what your true needs are and work on getting them met.</li>
    </ul>
  </div>

  <div class="col history">
    <h3>History doesn’t have to repeat itself!</h3>
    <p>The program is specifically designed for those of you who are ready to address the CORE ISSUES that prevent you from experiencing success, freedom and deep fulfilment in your relationships and in your life.</p>
  </div>

  <div class="col details">
    <h2 class="heading">Program Details</h2>
    <section>
      <h4>WHEN</h4>
      <p class="dates">Thursday 24th January 9:00am - 5:00pm<br>Friday, 25th January 9:00am – 5:00pm<br>Saturday, 26th January 9:00am – 5:00pm<br>Sunday, 27th January 9:00am – 5:00pm<br>Monday, 28th October 9:00am – 5:00pm</p>
      <p style="margin-top:9px">Enrolments close Friday, 18th January 2019. To book your place, register your interest or find out more about this program please call Marjorie 0491 570 156.</p>
    </section>
    <div class="rule"></div>
    <section>
      <h4>INCLUSIONS</h4>
      <p style="text-align:left">A pre-program phone consult Relevant on online diagnostic survey’s<br>Integrated Equine Assisted Psychotherapy<br>Art Therapy Piece<br>All course materials (notebook, writing materials), Morning and afternoon tea daily + light lunch</p>
    </section>
    <div class="rule"></div>
    <section><h4>INVESTMENTS : $2400 including GST</h4></section>
    <div class="rule"></div>
    <section>
      <h4>TERMS &amp; CONDITIONS</h4>
      <p>A non-refundable deposit of $800 is required to hold your place. Full payment is required by Friday 18th January 2019. Amberline transactions incur a 3.3% merchant fee, Vantra and Meridian Card 2.5%. DirectPay facility available.</p>
    </section>
  </div>

  <footer class="footer">
    The Tallowood Group Pty Ltd.<br>
    ABN 41 302 118 764 Fernhill Road, Ashby NSW 2799<br>
    Phone: 0491 570 156<br>
    Email: marjorie@thetallowoodgroup.example
  </footer>
  <div class="brand"><i></i><span>Tallowood Group</span></div>
</article>

</body>
</html>
```